Sign Design for Truck Repair Shop center

Need a road-side sign for a pickup truck repair shop called Torvane Garage. The logo is attached and should be used on the sign. The background should be white and the main part of the logo should take up a large part of the sign so it can be easily read by passing traffic. The sign is 4 feet tall by 8 feet wide. Also need to add the website address" "www.TorvaneGarage-example.com" and "Call/Text 555.013.4782"

```html
<!DOCTYPE html>
<html lang="en">
<head>
<meta charset="utf-8">
<title>Torvane Garage – Roadside Sign</title>
<link href="https://fonts.googleapis.com/css2?family=Bebas+Neue&family=Montserrat:wght@800&display=swap" rel="stylesheet">
<style>
  :root {
    --backdrop: #e3e3e3;
    --sign-white: #ffffff;
    --brand-blue: #0b54a3;
    --ink: #111111;
    --screw-metal: #c9ccd0;
    --screw-edge: #7d8288;
  }
  html, body {
    margin: 0;
    padding: 0;
    width: 800px;
    height: 1200px;
    overflow: hidden;
    background: var(--backdrop);
  }
  .canvas {
    position: relative;
    width: 800px;
    height: 1200px;
  }
  .sign {
    position: absolute;
    left: 76px;
    top: 437px;
    width: 650px;
    height: 325px;
    background: var(--sign-white);
    box-shadow: 0 6px 14px rgba(0,0,0,0.22);
    overflow: hidden;
  }
  .sign__band {
    position: absolute;
    inset: 0;
    width: 650px;
    height: 325px;
  }
  .sign__name {
    position: absolute;
    left: 0;
    right: 0;
    top: 54px;
    margin: 0;
    text-align: center;
    font-family: "Bebas Neue", Impact, sans-serif;
    font-weight: 400;
    font-size: 84px;
    line-height: 1;
    letter-spacing: 2px;
    color: var(--sign-white);
  }
  .sign__call {
    position: absolute;
    left: 0;
    right: 0;
    top: 206px;
    margin: 0;
    text-align: center;
    font-family: "Bebas Neue", Impact, sans-serif;
    font-size: 70px;
    line-height: 1;
    white-space: nowrap;
  }
  .sign__call-label { color: var(--brand-blue); }
  .sign__call-number { color: var(--ink); }
  .sign__web {
    position: absolute;
    left: 0;
    right: 0;
    top: 272px;
    margin: 0;
    text-align: center;
    font-family: "Montserrat", Arial, sans-serif;
    font-weight: 800;
    font-size: 24px;
    letter-spacing: 1px;
    line-height: 1;
    white-space: nowrap;
    color: var(--ink);
  }
  .screw {
    position: absolute;
    width: 16px;
    height: 16px;
  }
  .screw--tl { left: 18px; top: 19px; }
  .screw--tr { right: 20px; top: 19px; }
  .screw--bl { left: 18px; top: 289px; }
  .screw--br { right: 20px; top: 289px; }
</style>
</head>
<body>
<main class="canvas">
  <section class="sign" aria-label="Torvane Garage roadside sign">
    <svg class="sign__band" viewBox="0 0 650 325" aria-hidden="true">
      <polygon points="0,0 650,0 650,174 325,200 0,174" fill="var(--brand-blue)"/>
    </svg>

    <h1 class="sign__name">Torvane Garage</h1>

    <p class="sign__call">
      <span class="sign__call-label">Call/Text-</span>
      <span class="sign__call-number">555.013.4782</span>
    </p>

    <p class="sign__web">www.TorvaneGarage-example.com</p>

    <svg class="screw screw--tl" viewBox="0 0 16 16" aria-hidden="true">
      <circle cx="8" cy="8" r="7" fill="var(--screw-metal)" stroke="var(--screw-edge)" stroke-width="1.2"/>
      <path d="M8 4.5v7M4.5 8h7" stroke="#444" stroke-width="1.4"/>
    </svg>
    <svg class="screw screw--tr" viewBox="0 0 16 16" aria-hidden="true">
      <circle cx="8" cy="8" r="7" fill="var(--screw-metal)" stroke="var(--screw-edge)" stroke-width="1.2"/>
      <path d="M8 4.5v7M4.5 8h7" stroke="#444" stroke-width="1.4"/>
    </svg>
    <svg class="screw screw--bl" viewBox="0 0 16 16" aria-hidden="true">
      <circle cx="8" cy="8" r="7" fill="var(--screw-metal)" stroke="var(--screw-edge)" stroke-width="1.2"/>
      <path d="M8 4.5v7M4.5 8h7" stroke="#444" stroke-width="1.4"/>
    </svg>
    <svg class="screw screw--br" viewBox="0 0 16 16" aria-hidden="true">
      <circle cx="8" cy="8" r="7" fill="var(--screw-metal)" stroke="var(--screw-edge)" stroke-width="1.2"/>
      <path d="M8 4.5v7M4.5 8h7" stroke="#444" stroke-width="1.4"/>
    </svg>
  </section>
</main>
</body>
</html>
```